Medical centre needs a business card

We are a medcial centre in Australia, needing a new business card. Our demographic is low working class families. We are going to be renovating our premises to modernise the look and also had a new logo done a few months ago representing quality and community, and now need to update our cards. It needs to be doubled sided, with logo and contact details on the front, and appointment details on the back. . Needs to be modern and simple, easy to read. <br/><br/>Name: Fern Vale Medical Centre <br/>Address: 512 Kestrel Rd (Cnr Kestrel Rd & Lindon Park Rd),<br/>Corvane Court Shopping Centre, Paralowie, SA 5108<br/>Ph: 08 8361 4027<br/>Tag line: Where every visit counts for you<br/>Website: www.fernvalemedicalcentre.example.au<br/>Online bookings also available<br/><br/>(On the back, to have 3 lines of appointments that can be written in.<br/>Day, date, time)<br/><br/>Your next appointment is on<br/>Can try “M T W Th F Sa Su _________________ at ____________ am/pm” or other combinations <br/>Please advise as soon as possible if unable to attend<br/>Cancellation fees apply if less than 2 hrs notice<br/>Online appointments available (please highlight this option by either by position, colour or font)

Target Market(s)

Lower social economic working class, young families to seniors

Industry/Entity Type

Medical Centre

Contact Information for Business Card

Fern Vale Medical Centre
512 Kestrel Rd (Cnr Kestrel Rd & Lindon Park Drive)
Corvane Court Shopping Centre
Ellerby SA 5177
Ph: 08 8361 4027
www.fernvalemedicalcentre.example.au
Tagline line: where every visit counts for you
Back side is for appointments
Your next appointment is with Dr ______________
Day/date/time (Please give 3 lines of appointments)
Please advise as soon as possible if unable to attend
Cancellation fees apply if less than 2 hours notice
Online appointments available
Book online easily and conveniently (please highlight online appointments)

Font styles to use
Serif
Sans Serif

Colors

Designer to choose colors to be used in the design.

Requirements
Must have
• Modern and simple
• Easy to ready
• Induces a wellbeing feeling
• Incorporate our logo colours and feel from logo
• Induces feeling of stability and security
Nice to have
• Attract attention
• Pleasant to look at
• Feeling of innovation
Should not have
• Loud clashing colours
• Overly luxurious feeling
• Overly artistic

```html
<!DOCTYPE html>
<html lang="en">
<head>
<meta charset="utf-8">
<title>Fern Vale Medical Centre – Business Card</title>
<link href="https://fonts.googleapis.com/css2?family=Josefin+Sans:wght@400;600&family=Montserrat:wght@400;500;700&display=swap" rel="stylesheet">
<style>
  :root {
    --stage: #9c9c9c;
    --card: #ffffff;
    --blue: #1a7cc8;
    --blue-deep: #0f63b4;
    --blue-light: #3aa6e2;
    --green: #8cc63f;
    --grey-text: #7a7a7a;
    --rule: #9a9a9a;
  }
  * { box-sizing: border-box; margin: 0; padding: 0; }
  html, body { width: 1200px; height: 930px; overflow: hidden; }
  body {
    background: radial-gradient(circle at 55% 45%, #bdbdbd 0%, var(--stage) 70%);
    font-family: "Montserrat", sans-serif;
    position: relative;
  }
  .card {
    position: absolute;
    width: 520px;
    height: 318px;
    background: var(--card);
    border-radius: 22px;
    overflow: hidden;
    box-shadow: 0 6px 14px rgba(0,0,0,.25);
  }
  .card--back { left: 80px; top: 100px; }
  .card--front { left: 600px; top: 500px; }

  .brand-name {
    font-family: "Montserrat", sans-serif;
    font-weight: 700;
    color: var(--blue);
    text-transform: uppercase;
    letter-spacing: .5px;
    line-height: 1.1;
  }

  /* back: appointment side */
  .card--back .brand-name {
    position: absolute; left: 40px; top: 34px;
    font-size: 24px;
  }
  .appointment {
    position: absolute; left: 40px; top: 100px; right: 36px;
  }
  .appointment__lead {
    color: var(--blue); font-size: 14px; font-weight: 500;
    display: flex; align-items: flex-end; gap: 8px;
  }
  .appointment__field {
    display: flex; align-items: flex-end; gap: 10px;
    color: var(--grey-text); font-size: 13px; margin-top: 14px;
  }
  .write-line { flex: 1; border-bottom: 1px solid var(--rule); height: 1px; }
  .appointment__lead .write-line { border-color: var(--blue); }
  .appointment__notes {
    margin-top: 20px; color: var(--grey-text); font-size: 12.5px; line-height: 1.45;
  }
  .appointment__online { color: var(--green); font-weight: 700; }

  /* front: contact side */
  .card--front .band { position: absolute; inset: 0; }
  .card--front .brand {
    position: absolute; left: 120px; top: 58px;
    display: flex; align-items: center; gap: 12px;
  }
  .brand__mark { width: 34px; height: 34px; background: var(--blue); border-radius: 4px; }
  .card--front .brand-name { font-size: 20px; }
  .contact {
    position: absolute; left: 30px; right: 28px; bottom: 24px;
    color: #fff; font-family: "Josefin Sans", sans-serif; text-transform: uppercase;
    text-align: right; white-space: nowrap;
  }
  .contact__tagline { font-size: 14px; letter-spacing: 1px; margin-bottom: 6px; }
  .contact__rule { border-top: 1px solid rgba(255,255,255,.8); margin: 6px 0; }
  .contact__line { font-size: 11.5px; letter-spacing: .3px; line-height: 1.6; }
</style>
</head>
<body>

<section class="card card--back" aria-label="Appointment side">
  <div class="brand-name">Fern Vale<br>Medical Centre</div>
  <div class="appointment">
    <p class="appointment__lead">Your next appointment is with Dr <span class="write-line"></span></p>
    <p class="appointment__field">Day <span class="write-line"></span></p>
    <p class="appointment__field">Date <span class="write-line"></span></p>
    <p class="appointment__field">Time <span class="write-line"></span></p>
    <p class="appointment__notes">
      Please advise as soon as possible if unable to attend<br>
      Cancellation fees apply if less than 2 hours notice<br>
      <span class="appointment__online">Online appointments available.</span>
    </p>
  </div>
</section>

<section class="card card--front" aria-label="Contact side">
  <svg class="band" width="520" height="318" viewBox="0 0 520 318" aria-hidden="true">
    <defs>
      <linearGradient id="bandFill" x1="0" y1="0" x2="1" y2="1">
        <stop offset="0" stop-color="#4db3e8"/>
        <stop offset="1" stop-color="#0f63b4"/>
      </linearGradient>
    </defs>
    <path d="M0,258 Q200,150 520,118 L520,318 L0,318 Z" fill="url(#bandFill)"/>
    <path d="M0,250 Q200,142 520,110" fill="none" stroke="#8cc63f" stroke-width="4"/>
  </svg>
  <div class="brand">
    <span class="brand__mark"></span>
    <span class="brand-name">Fern Vale<br>Medical Centre</span>
  </div>
  <div class="contact">
    <p class="contact__tagline">Where every visit counts for you</p>
    <div class="contact__rule"></div>
    <p class="contact__line">P : 08 8361 4027 | W : www.fernvalemedicalcentre.example.au</p>
    <div class="contact__rule"></div>
    <p class="contact__line">512 Kestrel Rd (Cnr Kestrel Rd &amp; Lindon Park Drive)</p>
    <p class="contact__line">Corvane Court Shopping Centre Ellerby SA 5177</p>
  </div>
</section>

</body>
</html>
```